Namecard with Logo for NanoTechnology Business

We wish to invite you to propose a creative Logo design compatible with the namecard design that suits our business. (you may take inspiration from fullerene's molecular structure, but since one of our partner company already has a fullerene-logo, please don't propose anything similar to those. see attached image logo of "RAB")
You do not have to be constrained by a 'ball shaped' design requirement. You can play with the idea of a molecule, but high tech and creative.

Target Market(s)

lubricant market

Contact Information for Business Card

For the Front, instead of accentuating the company name, we would like instead to display the following words more prominently and creatively stylized and centered.

"Total Care Surface Reconditioning" (these words bigger)
"make your engine new again" (these words smaller and right below the words above, and with small letters)

The following contact details can be smaller compared to the emphasis above

Name detail: Owen Pratt
Company detail: Velbor Quill Singapore Pte Ltd
Headquarter detail: 27 Korvel Commerce Loop B, S530194
Mobile detail: (65) 83297150
Website: (to be confirmed)

For the Back of the namecard, there are to be two headings. Many words involved. Okay for the words to be smaller. Two columns please.

Column Heading#1; Market Sectors
Indented Words;
Bearings
Fleet Management
Trucks and Buses
Conveyor Systems
Gears and Gear Boxes
Heavy Machinery
Mining
Oil and Gas Drilling
Metal Forming
Steel Mills
Power Generation Plants
Railroad
Moving Freight
Space and Defence Industry
Wind Turbines

Column Heading#2; Oil Quality Research Laboratory for Condition Monitoring of Wear and Tear Sampling Analysis
Indented words;
Spectrographic Analysis
Infra-Red Spectroscopy
Karl Fischer Titration (H2O Content)
Viscosity Analysis
Ferrous Debris Monitoring
ISO 4406 Cleanliness Code
Wear Debris Analysis

We wish to include the logo of our partner companies (bottom of back)

Logo 1 - RAB Logo, with the accompanying words (Sole-Source Patented Technology)

Logo 2 - Quorvalent Logo, with the accompany words (Preferred Knowledge Partner)

Colors

Designer to choose colors to be used in the design.

Requirements
Must have
• words as provided
Nice to have
• the key to this project is a creative logo that suits our business
Should not have
• logo similar to attached

```html
<!DOCTYPE html>
<html lang="en">
<head>
<meta charset="utf-8">
<title>Velbor Quill – Business Card</title>
<link href="https://fonts.googleapis.com/css2?family=Exo+2:wght@500;700&family=Open+Sans:wght@400;600&display=swap" rel="stylesheet">
<style>
  :root {
    --backdrop: #d9d6d0;
    --card-black: #0b0b0b;
    --card-graphite: #2a2a2a;
    --ink-white: #f4f4f4;
    --ink-grey: #c9c9c9;
    --accent-yellow: #ffd400;
    --accent-yellow-light: #ffe55a;
  }
  * { margin: 0; padding: 0; box-sizing: border-box; }
  html, body {
    width: 1200px; height: 1023px; overflow: hidden;
    background: var(--backdrop);
  }
  .canvas {
    width: 1200px; height: 1023px;
    display: flex; flex-direction: column; align-items: center; justify-content: center;
    gap: 34px;
  }
  .card {
    position: relative; width: 820px; height: 455px; flex: none;
    background: radial-gradient(ellipse at 38% 62%, var(--card-graphite) 0%, var(--card-black) 58%);
    box-shadow: 0 14px 32px rgba(0,0,0,0.35);
    overflow: hidden;
    color: var(--ink-white);
  }

  /* Front */
  .headline {
    position: absolute; left: 48px; top: 44px; right: 40px;
    font-family: "Exo 2", sans-serif; font-weight: 500;
    font-size: 40px; letter-spacing: 0.5px; white-space: nowrap;
  }
  .brand { position: absolute; left: 110px; top: 190px; }
  .brand-name {
    font-family: "Exo 2", sans-serif; font-weight: 700;
    font-size: 38px; line-height: 1;
  }
  .brand-sub {
    font-family: "Exo 2", sans-serif; font-weight: 500;
    font-size: 21px; letter-spacing: 2px; margin-top: 3px;
  }
  .divider {
    position: absolute; left: 418px; top: 160px;
    width: 1.5px; height: 150px; background: var(--ink-grey);
  }
  .contact { position: absolute; left: 448px; top: 166px; font-family: "Open Sans", sans-serif; }
  .contact-name {
    font-family: "Exo 2", sans-serif; font-weight: 500;
    font-size: 25px; margin-bottom: 8px;
  }
  .contact-line {
    display: flex; align-items: center; gap: 10px;
    font-size: 14.5px; line-height: 1.7; white-space: nowrap;
  }
  .contact-line svg { width: 16px; height: 16px; flex: none; }
  .accent-band {
    position: absolute; left: 0; right: 0; top: 352px; height: 46px;
    background: linear-gradient(90deg, var(--accent-yellow-light), var(--accent-yellow));
  }

  /* Back */
  .column { position: absolute; top: 30px; font-family: "Open Sans", sans-serif; }
  .column-sectors { left: 42px; width: 300px; }
  .column-lab { left: 360px; width: 420px; }
  .column-heading {
    font-family: "Open Sans", sans-serif; font-weight: 600;
    font-size: 15px; line-height: 1.3; color: var(--accent-yellow);
    margin-bottom: 8px;
  }
  .item-list { list-style: none; }
  .item-list li {
    position: relative; padding-left: 18px;
    font-size: 12.5px; line-height: 16.5px; color: var(--ink-white);
  }
  .item-list li::before {
    content: ""; position: absolute; left: 2px; top: 5px;
    width: 6px; height: 6px; border-left: 2px solid var(--accent-yellow);
    transform: skewX(-20deg);
  }
  .partners {
    position: absolute; left: 42px; right: 42px; top: 350px; height: 70px;
    display: flex; align-items: center; justify-content: center; gap: 40px;
  }
  .partner { display: flex; align-items: center; gap: 14px; }
  .partner-badge {
    width: 48px; height: 48px; border-radius: 50%;
    background: #3a3a3a; border: 1.5px solid var(--ink-grey); flex: none;
  }
  .partner-caption {
    font-family: "Open Sans", sans-serif; font-size: 11.5px; font-weight: 600;
    letter-spacing: 1px; text-transform: uppercase; line-height: 1.4; color: var(--ink-grey);
  }
  .partner-divider { width: 1.5px; height: 56px; background: var(--ink-grey); }
</style>
</head>
<body>
<div class="canvas">
  <section class="card card-front">
    <h1 class="headline">Total Care Surface Reconditioning</h1>

    <div class="brand">
      <div class="brand-name">VELBOR QUILL</div>
      <div class="brand-sub">SINGAPORE PTE LTD</div>
    </div>

    <div class="divider"></div>

    <div class="contact">
      <div class="contact-name">Owen Pratt</div>
      <div class="contact-line">
        <svg viewBox="0 0 20 20" aria-hidden="true"><rect x="3" y="5" width="14" height="11" rx="1.5" fill="none" stroke="#ffd400" stroke-width="2"/></svg>
        <span>(65) 83297150</span>
      </div>
      <div class="contact-line">
        <svg viewBox="0 0 20 20" aria-hidden="true">
          <circle cx="10" cy="10" r="8" fill="#ffd400"/>
          <path d="M2 10h16M10 2c-3 3-3 13 0 16M10 2c3 3 3 13 0 16M4 6h12M4 14h12" stroke="#0b0b0b" stroke-width="1" fill="none"/>
        </svg>
        <span>www.yourdomain.com</span>
      </div>
      <div class="contact-line">
        <svg viewBox="0 0 20 20" aria-hidden="true"><path d="M10 1a6 6 0 0 0-6 6c0 5 6 12 6 12s6-7 6-12a6 6 0 0 0-6-6z" fill="#ffd400"/><circle cx="10" cy="7" r="2.2" fill="#0b0b0b"/></svg>
        <span>27 Korvel Commerce Loop B, S530194</span>
      </div>
    </div>

    <div class="accent-band"></div>
  </section>

  <section class="card card-back">
    <div class="column column-sectors">
      <h2 class="column-heading">Market Sectors</h2>
      <ul class="item-list">
        <li>Bearings</li>
        <li>Fleet Management</li>
        <li>Trucks and Buses</li>
        <li>Conveyor Systems</li>
        <li>Gears and Gear Boxes</li>
        <li>Heavy Machinery</li>
        <li>Mining</li>
        <li>Oil and Gas Drilling</li>
        <li>Metal Forming</li>
        <li>Steel Mills</li>
        <li>Power Generation Plants</li>
        <li>Railroad</li>
        <li>Moving Freight</li>
        <li>Space and Defence Industry</li>
        <li>Wind Turbines</li>
      </ul>
    </div>

    <div class="column column-lab">
      <h2 class="column-heading">Oil Quality Research Laboratory for Condition Monitoring of Wear and Tear Sampling Analysis</h2>
      <ul class="item-list">
        <li>Spectrographic Analysis</li>
        <li>Infra-Red Spectroscopy</li>
        <li>Karl Fischer Titration (H2O Content)</li>
        <li>Viscosity Analysis</li>
        <li>Ferrous Debris Monitoring</li>
        <li>ISO 4406 Cleanliness Code</li>
        <li>Wear Debris Analysis</li>
      </ul>
    </div>

    <div class="partners">
      <div class="partner">
        <div class="partner-badge" role="img" aria-label="Partner badge"></div>
        <div class="partner-caption">Sole-Source<br>Patented Technology</div>
      </div>
      <div class="partner-divider"></div>
      <div class="partner">
        <div class="partner-badge" role="img" aria-label="Partner badge"></div>
        <div class="partner-caption">Preferred<br>Knowledge Partner</div>
      </div>
    </div>
  </section>
</div>
</body>
</html>
```